Redesign Our Presentation on Rational Prescribing

We are looking for a new designer for QVMed, a project that creates educational modules for healthcare providers in the District of Columbia (more information at hlb.example-gov.org/qvmed). We want someone to redesign our powerpoints to look clean and professional, with original graphics that reflect the content on the slides. We also want someone who is creative and could potentially also redesign factsheets, written reports, and promotional postcards.

All the text on the slides must stay the same and it must be in the template (red line at the top, with the red box at the bottom, with the Harlow Bureau of Wellness logo). We want a powerpoint that features original graphics, looks professional, looks clean and is easy to read.

Industry/Entity Type

Healthcare

```html
<!DOCTYPE html>
<html lang="en">
<head>
<meta charset="utf-8">
<title>QVMed – Rational Prescribing Slides</title>
<link href="https://fonts.googleapis.com/css2?family=Lato:ital,wght@0,300;0,400;0,700;0,900;1,300;1,400;1,700&display=swap" rel="stylesheet">
<style>
  :root{
    --bg:#e4e4e4;
    --slide:#ffffff;
    --red:#e8202a;
    --navy:#2c2a6b;
    --purple:#5b568f;
    --coral:#ee5a5f;
    --gold:#b8953c;
    --ink:#3a3a3a;
    --muted:#6b6b6b;
    --beige:#efe3cc;
    --grey-box:#eeeef1;
    --mint:#c9f3d8;
    --blush:#f8c5c5;
    --card:rgba(255,255,255,0.82);
  }
  *{box-sizing:border-box;margin:0;padding:0}
  html,body{width:1200px;height:1000px;overflow:hidden}
  body{background:var(--bg);font-family:'Lato',sans-serif;color:var(--ink);position:relative}
  .slide{position:absolute;width:522px;height:292px;background:var(--slide);overflow:hidden;box-shadow:0 2px 6px rgba(0,0,0,.18)}
  .s3{left:53px;top:182px}.s5{left:625px;top:182px}.s2{left:53px;top:523px}.s6{left:625px;top:523px}
  .title{position:absolute;left:41px;top:21px;font-size:15px;font-weight:300;color:#333;letter-spacing:.2px}
  .rule{position:absolute;left:28px;right:0;top:43px;height:1.5px;background:var(--red)}
  .page-no{position:absolute;right:7px;top:7px;width:16px;height:16px;border-radius:3px;background:var(--navy);color:#fff;font-size:7px;display:flex;align-items:center;justify-content:center}
  .footer{position:absolute;left:0;right:0;bottom:0;height:16px;background:var(--red);color:#fff;font-size:7px;font-style:italic;padding-left:17px;line-height:16px}
  .brand{position:absolute;left:17px;bottom:22px;display:flex;align-items:center;gap:3px;font-size:11px;font-weight:900;color:var(--navy)}
  .brand .dot{width:7px;height:7px;border-radius:50%;background:var(--navy)}
  .box{position:absolute}
  .note{background:var(--beige);font-size:9px;line-height:1.25;color:#444;padding:6px 6px}
  .note .b{color:var(--red)}
  .example{background:var(--grey-box);padding:5px 9px;font-size:5.6px;line-height:1.35;color:#666;text-align:justify}
  .example h4{font-size:9px;font-style:italic;font-weight:700;color:var(--navy);margin-bottom:2px}
  .chev{position:absolute}
  /* slide 5 */
  .panel-green{left:27px;top:62px;width:152px;height:182px;background:var(--mint)}
  .panel-pink{left:194px;top:62px;width:300px;height:182px;background:var(--blush)}
  .green-text{position:absolute;left:10px;right:10px;top:70px;text-align:center;font-size:9.5px;line-height:1.35;color:#444}
  .avoid{position:absolute;left:64px;top:20px;font-size:12px;font-weight:700;color:var(--red)}
  .pink-list{position:absolute;left:64px;top:38px;width:228px;font-size:8.2px;line-height:1.35;color:#444;list-style:none}
  .pink-list li{margin-bottom:14px;padding-left:8px;position:relative}
  .pink-list li::before{content:"•";color:var(--red);position:absolute;left:0}
  .pink-list .sub{font-size:6px;color:#555;margin-top:-6px;padding-left:10px}
  .pink-list .sub::before{content:"›";font-weight:900;font-size:9px;top:-3px}
  /* slide 2 */
  .quote{position:absolute;left:30px;top:78px;width:173px;text-align:right;font-size:13px;font-style:italic;font-weight:300;line-height:1.18;color:#444}
  .dots{position:absolute;left:211px;top:60px;height:182px;border-left:2.5px dotted #c9c9c9}
  .stat{position:absolute;left:228px;display:flex;align-items:flex-end;gap:2px}
  .stat .bgshape{position:absolute;left:0;top:-4px;width:64px;height:44px;background:#f1f1f1;border-radius:2px 30px 2px 2px}
  .stat .pct{position:relative;font-size:30px;font-weight:900;line-height:1}
  .stat .lbl{position:relative;font-size:7.5px;color:#555;margin-bottom:4px}
  .stat .lbl b{font-weight:900}
  .cite{position:absolute;right:25px;top:232px;font-size:7.5px;font-style:italic;color:#555}
  /* slide 6 */
  .s6 .backdrop{position:absolute;inset:0;background:radial-gradient(circle at 30% 30%,#f4d6d6 0%,#e9b7b8 40%,#d98c8f 75%,#c96a6e 100%)}
  .s6 .title,.s6 .rule{z-index:2}
  .card{position:absolute;top:64px;width:152px;height:182px;background:var(--card);display:flex;align-items:center;justify-content:center;text-align:center;color:#444}
  .card .motif{position:absolute;width:60px;height:60px;border-radius:50%;background:rgba(232,140,145,.45);left:46px;top:61px}
  .card p{position:relative;font-size:10px;line-height:1.3;padding:0 10px}
  .card p b{color:var(--red)}
  .risk{font-size:6px;line-height:1.32;color:#444;position:relative}
  .risk span{display:block}
  .risk span::after{content:" •";color:var(--red)}
  .risk .head::after{content:""}
</style>
</head>
<body>

<!-- Slide 3: Predicting ADRs -->
<section class="slide s3">
  <h2 class="title">Predicting ADRs.</h2>
  <div class="rule"></div>
  <div class="page-no">3</div>

  <svg class="chev" style="left:68px;top:66px" width="22" height="34" viewBox="0 0 22 34"><path d="M3 3 L17 17 L3 31" fill="none" stroke="var(--purple)" stroke-width="6" stroke-linecap="round" stroke-linejoin="round"/></svg>
  <div class="box note" style="left:92px;top:60px;width:228px;height:52px;padding-top:10px">
    <span class="b">•</span> Few ADRs represent improper prescribing.<br>
    <span class="b">•</span> Most ADRs are related to the pharmacologic properties of a drug.
  </div>
  <div class="box example" style="left:320px;top:58px;width:180px;height:88px">
    <h4>For example:</h4>
    Benzodiazepines cause increased imbalance and gait instability associated with increased risk of falls. A patient taking a nightly benzodiazepine to induce sleep is at high risk for falls. All subsequent health-care costs and associated debility are due to the prescribed medication.
  </div>

  <svg class="chev" style="left:24px;top:163px" width="22" height="34" viewBox="0 0 22 34"><path d="M3 3 L17 17 L3 31" fill="none" stroke="var(--coral)" stroke-width="6" stroke-linecap="round" stroke-linejoin="round"/></svg>
  <div class="box note" style="left:50px;top:170px;width:188px;height:34px;padding-top:3px">
    <span class="b">•</span> Many ADRs are both predictable and avoidable (Dalton &amp; Marsh 2015).
  </div>
  <div class="box example" style="left:245px;top:165px;width:220px;height:97px">
    <h4 style="color:var(--red)">For example:</h4>
    Anticholinergic medications prescribed to control bladder spasm may result in constipation and even mental status changes. These are expected outcomes from modulating acetylcholine levels. This type of drug-associated adverse effect raises the risk of prescribing additional medications, such as constipation-relieving agents, to address adverse effects of the original drug. Eliminating, changing, or lowering the dose of the original drug is the right course of action.
  </div>

  <div class="brand"><span class="dot"></span>HBW</div>
  <div class="footer">hlb.example-gov.org</div>
</section>

<!-- Slide 5: Best Drugs in Diabetic Elders -->
<section class="slide s5">
  <h2 class="title">Best Drugs in Diabetic Elders</h2>
  <div class="rule"></div>
  <div class="page-no">5</div>

  <div class="box panel-green">
    <svg style="position:absolute;left:50px;top:12px" width="52" height="44" viewBox="0 0 52 44" fill="none" stroke="#fff" stroke-width="1.6">
      <rect x="4" y="8" width="30" height="14" rx="7" transform="rotate(-35 19 15)"/>
      <line x1="14" y1="22" x2="22" y2="10"/>
      <circle cx="36" cy="29" r="10"/>
      <line x1="29" y1="36" x2="43" y2="22"/>
    </svg>
    <p class="green-text">Only metformin should be used to achieve hemoglobin A1c &lt; 7.5% in most older adults with type 2 diabetes.</p>
  </div>

  <div class="box panel-pink">
    <svg style="position:absolute;left:14px;top:14px" width="36" height="36" viewBox="0 0 36 36" fill="none" stroke="#fff" stroke-width="1.6" stroke-linecap="round">
      <rect x="9" y="9" width="10" height="20" rx="1" transform="rotate(45 14 19)"/>
      <line x1="22" y1="10" x2="28" y2="4"/><line x1="25" y1="1" x2="31" y2="7"/>
      <line x1="6" y1="28" x2="2" y2="32"/>
    </svg>
    <div class="avoid">AVOID INSULIN!</div>
    <ul class="pink-list">
      <li>Insulin-related hypoglycemia and errors are implicated in an estimated 9.2% of ED visits associated with ADE (Garrow et al 2014).</li>
      <li>This one preventable ADE accounts for nearly 100,000 ED Visits every year.</li>
      <li class="sub">Patients at or above the age of 80 were twice as likely to visit the ED and 5 times more likely to be hospitalized.</li>
    </ul>
  </div>

  <div class="brand"><span class="dot"></span>HBW</div>
  <div class="footer">hlb.example-gov.org</div>
</section>

<!-- Slide 2: Consequences of Multiple Medication Use -->
<section class="slide s2">
  <h2 class="title">Consequences of Multiple Medication Use.</h2>
  <div class="rule"></div>
  <div class="page-no">2</div>

  <p class="quote">The use of several medications simultaneously, even at otherwise appropriate doses, increases the risk of adverse effects, drug interactions,</p>
  <div class="dots"></div>

  <div class="stat" style="top:78px"><span class="bgshape"></span><span class="pct" style="color:var(--gold)">13%</span><span class="lbl">The risk of ADRs when taking <b style="color:var(--gold)">TWO</b> medicines.</span></div>
  <div class="stat" style="top:140px"><span class="bgshape"></span><span class="pct" style="color:var(--navy)">58%</span><span class="lbl">The risk of ADRs when taking <b style="color:var(--navy)">FIVE</b> medicines.</span></div>
  <div class="stat" style="top:199px"><span class="bgshape"></span><span class="pct" style="color:var(--red)">82%</span><span class="lbl">The risk of ADRs when taking <b style="color:var(--red)">SEVEN</b> medicines.</span></div>
  <p class="cite">(Dane 2015)</p>

  <div class="brand"><span class="dot"></span>HBW</div>
  <div class="footer">hlb.example-gov.org</div>
</section>

<!-- Slide 6: Antipsychotics -->
<section class="slide s6">
  <div class="backdrop" role="img" aria-label="Soft-focus photograph of red and white capsules"></div>
  <h2 class="title">Antipsychotics</h2>
  <div class="rule"></div>
  <div class="page-no">6</div>

  <div class="card" style="left:16px">
    <span class="motif" role="img" aria-label="Raised hand illustration"></span>
    <p>Antipsychotics should <b>NOT</b> be the first choice to treat behavioral and psychological symptoms of dementia.</p>
  </div>
  <div class="card" style="left:184px">
    <span class="motif" role="img" aria-label="Warning symbol illustration"></span>
    <div class="risk">
      <span class="head">Risks of antipsychotics include:</span>
      <span>Death</span><span>Strokes</span><span>Diabetes</span><span>Weight gain</span><span>Cognitive decline</span>
      <span>Neuroleptic malignant syndrome<br>(fever, autonomic instability, altered<br>mental state and extrapyramidal signs)</span>
      <span>Extrapyramidal effects</span><span>Hypothermia</span><span>Oversedation</span><span>Falls</span>
    </div>
  </div>
  <div class="card" style="left:352px">
    <span class="motif" role="img" aria-label="Head profile illustration"></span>
    <p style="font-size:11px">Antipsychotics may actually increase delirium</p>
  </div>

  <div class="footer">hlb.example-gov.org</div>
</section>

</body>
</html>
```